Create a Brochure Design for Harlow Senior Living

Harlow Senior Living is a subsidiary of the Harlow Care Group. This brochure is specifically for the Harlow Senior Living company and brand. Create a 3 panel, front and back, tri-fold brochure. This brochure will be a way to introduce our senior living care home to the community, prospective, clients, and various referral partners. It is modern and state of the art home. Like the home, the brochure must be eye catching, unique in its deliverables (as it doesn’t feel like a care facility) and demonstrate both attention to detail and comfort. Our organization is sophisticated and built around warmth, care and individualized personal attention. The most important aspect of this design is to focus on creating a nurturing, warm, and inviting feel where you would want to put your own loved ones in our care home.
I am open to the creativity of the designer to develop something based on the above criteria; however I would like the design to work well with the existing collateral material. What I mean by that is that while I want everything to have its own personality and stand out as its own brand representative, I still need to be able to tell that the overall design concept stays stylistically inside of the same ‘family’ of existing designed material. Because of this, below I would like for the designer to pull inspiration from the link to our website (Located below) as well as from the attachment of our recently refreshed business cards (Attached). This should allow each design to be unique and creative, while still staying inside of a framework and the feel/style that I am looking for.
Finally, I want all the designers to understand that this brochure design is for a facility where we are responsible to provide care for active, positive, and happy seniors/elders. We have care professionals and staff on-site to provide 24x7, around the clock, care to the elders and geriatric residents as it is needed and required. The photos that are used must represent aging gracefully and with elegance.
Target Market(s)
Seniors(50+), Caring Family Members, Social Workers, Physicians, Hospitals
Industry/Entity Type
Business
Requirements
Must have
- • The company logo must be included.
Nice to have
- Attached you will find a sampling of images related to the long term care industry. Please feel free to use your own images as you see fit. The interior care home pictures are of our actual facility and should be incorporated into the brochure and your design.
Company Information
• Look under the Harlow Senior Living tab at
www.harlowcaregroup.example.

```html
<!DOCTYPE html>
<html lang="en">
<head>
<meta charset="utf-8">
<title>Harlow Senior Living – Tri-fold Brochure</title>
<link rel="stylesheet" href="https://fonts.googleapis.com/css2?family=Raleway:wght@200;300;400;500&family=Open+Sans:wght@400;600&display=swap">
<style>
  :root{
    --stage:#3a3a3a;
    --paper:#ffffff;
    --ink:#1a1a1a;
    --black:#0b0b0b;
    --teal:#4a918c;
    --teal-soft:#8fc0bc;
    --grey-text:#8a8a8a;
    --fold:#e3e3e3;
    --photo-warm-a:#c79b62;
    --photo-warm-b:#6e4a2c;
    --photo-bath-a:#ece6d8;
    --photo-bath-b:#c9b48a;
  }
  *{box-sizing:border-box;margin:0;padding:0}
  html,body{width:1200px;height:794px;overflow:hidden}
  body{background:radial-gradient(ellipse at 50% 40%,#555 0%,var(--stage) 70%);font-family:"Open Sans",sans-serif;position:relative}

  .spread{position:absolute;top:176px;width:560px;height:442px;background:var(--paper);overflow:hidden;box-shadow:0 18px 40px rgba(0,0,0,.45)}
  .spread--outer{left:30px}
  .spread--inner{left:610px}
  .spread svg.art{position:absolute;inset:0;width:560px;height:442px}
  .fold{position:absolute;top:0;bottom:0;width:1px;background:var(--fold)}
  .fold--1{left:187px}.fold--2{left:373px}

  /* outer spread */
  .about{position:absolute;left:0;top:0;width:187px;height:442px;background:var(--black);color:#ddd;padding:40px 14px 0 16px}
  .about__title{font-family:"Raleway",sans-serif;font-weight:200;font-size:30px;color:#fff;letter-spacing:.5px;margin-bottom:12px}
  .about__text{font-size:6.2px;line-height:1.55;margin-bottom:9px;color:#cfcfcf}
  .photo-caption{position:absolute;font-family:"Raleway",sans-serif;font-weight:300;color:#fff;font-size:15px;line-height:1.05;opacity:.9}
  .photo-caption--suite{left:208px;top:178px}
  .photo-caption--home{left:390px;top:150px}

  .brand{display:flex;flex-direction:column;align-items:center;color:var(--teal);font-family:"Raleway",sans-serif;font-weight:400;text-align:center}
  .brand__mark{width:12px;height:12px;background:var(--teal);margin-bottom:4px}
  .brand--small{position:absolute;left:187px;width:186px;top:288px;font-size:10px}
  .brand--large{position:absolute;left:373px;width:187px;top:262px;font-size:17px;line-height:1.1}
  .brand--large .brand__mark{width:18px;height:18px;margin-bottom:6px}
  .contact{position:absolute;left:187px;width:186px;top:330px;text-align:center;font-family:"Raleway",sans-serif;font-weight:300;font-size:9.5px;line-height:1.5;color:var(--grey-text)}
  .phone-line{position:absolute;left:373px;width:187px;top:350px;text-align:center;font-size:12px;letter-spacing:.5px;color:var(--ink)}

  /* inner spread */
  .tagline{position:absolute;left:14px;top:240px;width:170px;font-family:"Raleway",sans-serif;font-weight:200;font-size:25px;line-height:1.1;color:var(--teal-soft)}
  .services{position:absolute;left:200px;top:222px;width:162px}
  .services__title{font-family:"Raleway",sans-serif;font-weight:300;font-size:17px;color:var(--teal);margin-bottom:2px}
  .body-copy{font-size:6.4px;line-height:1.5;color:#333;margin-bottom:7px}
  .life{position:absolute;left:386px;top:262px;width:160px}
  .quote{position:absolute;left:386px;top:372px;width:160px;font-family:"Raleway",sans-serif;font-style:italic;font-weight:400;font-size:8.5px;line-height:1.45;color:#333;text-align:right;padding:0 16px}
  .quote__mark{position:absolute;font-family:"Raleway",sans-serif;font-weight:500;font-size:34px;color:var(--teal);line-height:1;font-style:normal}
  .quote__mark--open{left:-2px;top:-10px}
  .quote__mark--close{right:-4px;bottom:-22px}
</style>
</head>
<body>

<section class="spread spread--outer" aria-label="Brochure outside">
  <svg class="art" viewBox="0 0 560 442" aria-hidden="false">
    <defs>
      <linearGradient id="lounge" x1="0" y1="0" x2="1" y2="1">
        <stop offset="0" stop-color="var(--photo-warm-a)"/>
        <stop offset="1" stop-color="var(--photo-warm-b)"/>
      </linearGradient>
      <clipPath id="roundFrame"><ellipse cx="330" cy="70" rx="230" ry="188"/></clipPath>
    </defs>
    <path d="M330 -120 A250 205 0 0 1 560 120 L560 -120 Z" fill="#fff"/>
    <path d="M150 70 A245 205 0 0 0 560 160 L560 60 A240 195 0 0 1 170 70 Z" fill="var(--black)"/>
    <path d="M420 -20 A200 220 0 0 1 540 250 A215 210 0 0 0 440 -20 Z" fill="var(--black)"/>
    <rect x="187" y="0" width="373" height="258" fill="url(#lounge)" clip-path="url(#roundFrame)" role="img" aria-label="Photo of the bright shared living room with sofas and open kitchen"/>
  </svg>
  <div class="fold fold--1"></div><div class="fold fold--2"></div>

  <div class="about">
    <h2 class="about__title">About US</h2>
    <p class="about__text">Harlow Care Group is proud to introduce a new kind of senior home. Harlow Senior Living was created for residents who want the comfort of home with support close at hand.</p>
    <p class="about__text">Our home was rebuilt in 2012 and offers ten private suites, each with its own bath, closet and window view. Suites range in size and may be furnished to suit each resident.</p>
    <p class="about__text">Common areas include a bright living room, dining room, kitchen, garden lanai and laundry. Every space is designed for safety, ease and warm daily company with friends.</p>
  </div>

  <p class="photo-caption photo-caption--suite">Choose<br>your private<br>suite</p>
  <p class="photo-caption photo-caption--home">Welcome<br>Home</p>

  <div class="brand brand--small"><span class="brand__mark"></span>Harlow Senior Living</div>
  <address class="contact">480 Palm Grove Ave, Suite 200<br>Harbor City HI 96700<br>Phone 555 014 22 70<br>Fax 555 014 2271<br>hello@harlowcare.example</address>

  <div class="brand brand--large"><span class="brand__mark"></span>Harlow<br>Senior Living</div>
  <p class="phone-line">555 014 22 70</p>
</section>

<section class="spread spread--inner" aria-label="Brochure inside">
  <svg class="art" viewBox="0 0 560 442">
    <defs>
      <linearGradient id="suites" x1="0" y1="0" x2="1" y2="0">
        <stop offset="0" stop-color="var(--photo-bath-a)"/>
        <stop offset=".5" stop-color="var(--photo-bath-b)"/>
        <stop offset="1" stop-color="var(--photo-warm-a)"/>
      </linearGradient>
    </defs>
    <path d="M0 0 H560 V168 C470 215 400 190 330 150 C250 105 150 80 0 120 Z" fill="url(#suites)" role="img" aria-label="Photos of an accessible bathroom and a furnished private bedroom suite"/>
    <path d="M0 120 C150 80 250 105 330 150 C400 190 470 215 560 168 V190 C470 235 400 212 330 172 C250 128 150 104 0 142 Z" fill="var(--black)"/>
    <path d="M0 142 C150 104 250 128 330 172 C400 212 470 235 560 190 V194 C470 240 400 218 330 178 C250 134 150 110 0 148 Z" fill="#9a9a9a"/>
  </svg>
  <div class="fold fold--1"></div><div class="fold fold--2"></div>

  <p class="tagline">Quality care.<br>Enrich your<br>lifestyle</p>

  <div class="services">
    <h2 class="services__title">Services</h2>
    <p class="body-copy">Harlow Senior Living is a unique care concept, designed around a social model which encourages “neighbors” to be as independent as possible, actively participate in life here, and interact with their fellow neighbors.</p>
    <p class="body-copy">Here, you’ll maintain purpose in life while having personal care assistance as needed, activities, exercise, transportation, and companionship. Professional staff will be in residence 24 hours a day. This is a very special home, offering you a loving and nurturing life experience.</p>
    <p class="body-copy">Stay busy doing what you love here! Participate in as many activities as you like and discover life anew. Keep up your favorite hobbies or take up new ones.</p>
  </div>

  <div class="life">
    <p class="body-copy">In our home, neighbors can do a little gardening, stay in touch with family and friends on social media, email, or by video calls, relax in the soaking tub, take up a new hobby, enjoy music and crafts, community outings, exercise programs, beach walks, movie nights, board games, barbecues, and a whole lot more.</p>
    <p class="body-copy">Harlow Senior Living is a home where neighbors are actively engaged, individuality is encouraged, and life has purpose. It’s a home!</p>
  </div>

  <blockquote class="quote">
    <span class="quote__mark quote__mark--open">“</span>
    Just bring your suitcase.<br>We’ll take care of the rest!
    <span class="quote__mark quote__mark--close">”</span>
  </blockquote>
</section>

</body>
</html>
```